Business card for auto dealership

Looking for a clean modern design.
Would like attached logo incorporated

Industry/Entity Type

Car dealership

Contact Information for Business Card

Name, website, phone, cell, fax, email

```html
<!DOCTYPE html>
<html lang="en">
<head>
<meta charset="utf-8">
<title>Hollis Truck &amp; Auto Sales – Business Card</title>
<link href="https://fonts.googleapis.com/css2?family=Lato:wght@400;700&display=swap" rel="stylesheet">
<style>
  :root {
    --canvas: #1c1c1e;
    --card: #f7f8f8;
    --card-white: #fbfbfb;
    --ink: #1a1a1a;
    --ink-soft: #555759;
    --rule: #8a8c8e;
    --pattern-light: #f1f1f1;
    --pattern-mid: #e2e2e2;
    --accent-cream: #f3edce;
    --accent-grey: #8d8d8d;
    --ghost: #ececec;
  }
  * { margin: 0; padding: 0; box-sizing: border-box; }
  html, body {
    width: 1200px; height: 936px; overflow: hidden;
    background: var(--canvas);
    font-family: 'Lato', sans-serif;
  }
  .stage { position: relative; width: 1200px; height: 936px; }

  .card {
    position: absolute;
    width: 540px; height: 308px;
    overflow: hidden;
    box-shadow: 0 10px 30px rgba(0,0,0,.5);
  }

  /* Front */
  .card--front { left: 50px; top: 150px; background: var(--card); }
  .front__pattern {
    position: absolute; inset: 0;
    background: linear-gradient(135deg, var(--pattern-light), var(--pattern-mid) 55%, var(--pattern-light));
  }
  .front__band {
    position: absolute; left: 0; right: 0; bottom: 0; height: 22px;
    background: var(--accent-cream);
  }
  .front__band-end {
    position: absolute; right: 0; bottom: 0; width: 14px; height: 22px;
    background: var(--accent-grey);
  }
  .brand {
    position: absolute;
    color: var(--ink);
    font-weight: 700;
    line-height: 1.05;
    text-align: center;
  }
  .card--front .brand {
    left: 0; right: 0; top: 108px; font-size: 42px;
  }
  .brand__sub { display: block; font-size: .42em; letter-spacing: .12em; margin-top: 6px; }

  /* Back */
  .card--back { left: 610px; top: 478px; background: var(--card-white); }
  .back__ghost {
    position: absolute; left: 150px; top: 120px;
    font-size: 92px; font-weight: 700; color: var(--ghost);
    white-space: nowrap;
  }
  .card--back .brand {
    left: 30px; top: 150px; font-size: 30px; text-align: left;
  }
  .back__edge {
    position: absolute; right: 0; top: 0; bottom: 0; width: 26px;
    background: linear-gradient(90deg, #b9b9b9, var(--accent-grey));
  }
  .back__divider {
    position: absolute; left: 268px; top: 70px; width: 1px; height: 150px;
    background: var(--rule);
  }
  .contact {
    position: absolute; left: 288px; top: 62px;
    color: var(--ink-soft);
  }
  .contact__name { font-size: 24px; font-weight: 400; letter-spacing: .02em; }
  .contact__title { font-size: 16px; margin-top: 2px; margin-bottom: 14px; }
  .contact__list { list-style: none; font-size: 13px; line-height: 1.75; }
  .contact__list li { display: flex; align-items: center; gap: 8px; }
  .contact__list svg { width: 11px; height: 11px; fill: var(--ink-soft); flex: none; }
</style>
</head>
<body>
<main class="stage">

  <section class="card card--front" aria-label="Card front">
    <div class="front__pattern" role="img" aria-label="Soft grey geometric hexagon background pattern"></div>
    <div class="front__band"></div>
    <div class="front__band-end"></div>
    <div class="brand">Hollis<span class="brand__sub">TRUCK &amp; AUTO SALES</span></div>
  </section>

  <section class="card card--back" aria-label="Card back">
    <div class="back__ghost" aria-hidden="true">Hollis</div>
    <div class="brand">Hollis<span class="brand__sub">TRUCK &amp; AUTO SALES</span></div>
    <div class="back__divider"></div>
    <div class="contact">
      <p class="contact__name">DEAN MARLOW</p>
      <p class="contact__title">president</p>
      <ul class="contact__list">
        <li>
          <svg viewBox="0 0 24 24" aria-hidden="true"><path d="M6.6 10.8a15 15 0 0 0 6.6 6.6l2.2-2.2c.3-.3.7-.4 1-.2 1.1.4 2.3.6 3.6.6.6 0 1 .4 1 1V20c0 .6-.4 1-1 1C10.6 21 3 13.4 3 4c0-.6.4-1 1-1h3.5c.6 0 1 .4 1 1 0 1.3.2 2.5.6 3.6.1.3 0 .7-.2 1z"/></svg>
          555- 218-3094
        </li>
        <li>
          <svg viewBox="0 0 24 24" aria-hidden="true"><path d="M2 5h20v14H2z M2 5l10 8 10-8" /></svg>
          dean.marlow@mailbox.com
        </li>
        <li>
          <svg viewBox="0 0 24 24" aria-hidden="true"><circle cx="12" cy="12" r="10"/></svg>
          HollisTruckAuto.com
        </li>
      </ul>
    </div>
    <div class="back__edge"></div>
  </section>

</main>
</body>
</html>
```